Telmoro Business Card

I already have the conplay logo. I need to develop a professional business card layout

Target Market(s)

Business

Industry/Entity Type

Business

Contact Information for Business Card

Company Name: Telmoro Limited

Font styles to use
Sans Serif

Colors

Designer to choose colors to be used in the design.

Requirements
Must have
• Use current logo
• Need two card size options:
• Small Card: 70mm x 28mm (Landscape)
• Square Card: 65mm x 65mm
Nice to have
• I will need 8-10 files for each name, number and email address (details to follow)

```html
<!DOCTYPE html>
<html lang="en">
<head>
<meta charset="utf-8">
<title>Telmoro Limited – Square Business Cards</title>
<link href="https://fonts.googleapis.com/css2?family=Montserrat:wght@400;500;700;800&family=Oswald:wght@400;500&display=swap" rel="stylesheet">
<style>
  :root{
    --bg:#dcdcdc;
    --paper:#f3f3f3;
    --green:#7bb33b;
    --orange:#e8951f;
    --ink:#2b2b2b;
    --white:#ffffff;
    --navy:#2a2f86;
    --blue:#2565b5;
    --sky:#35a0dc;
    --logo-blue:#2565b5;
  }
  *{margin:0;padding:0;box-sizing:border-box}
  html,body{width:1200px;height:1185px;overflow:hidden}
  body{background:var(--bg);position:relative;font-family:"Montserrat",sans-serif}
  .card{position:absolute;top:332px;width:520px;height:520px;border-radius:40px;overflow:hidden;background:var(--paper);box-shadow:0 10px 24px rgba(0,0,0,.18)}
  .card--front{left:50px}
  .card--back{left:630px}
  .card__art{position:absolute;inset:0}

  /* front card */
  .front-logo{position:absolute;left:40px;top:38px;color:var(--white)}
  .front-logo__name{font-weight:800;font-size:44px;letter-spacing:1px;line-height:1}
  .front-logo__sub{font-weight:500;font-size:13px;letter-spacing:6px;color:var(--ink);margin-top:8px}
  .front-contact{position:absolute;left:40px;top:222px;list-style:none;color:var(--ink)}
  .front-contact li{display:flex;align-items:baseline;font-size:20px;margin-bottom:16px}
  .front-contact li:nth-child(2){padding-left:22px}
  .front-contact li:nth-child(3){padding-left:58px}
  .front-contact li:nth-child(4){padding-left:80px}
  .front-contact__key{font-weight:800;font-size:28px;width:34px}

  /* back card */
  .back-logo{position:absolute;left:40px;top:48px;color:var(--logo-blue)}
  .back-logo__name{font-weight:800;font-size:46px;letter-spacing:1px;line-height:1}
  .back-logo__sub{font-weight:500;font-size:13px;letter-spacing:6px;margin-top:8px}
  .back-contact{position:absolute;left:40px;bottom:70px;list-style:none;font-family:"Oswald",sans-serif;color:var(--ink);font-size:19px;letter-spacing:1px;text-transform:uppercase;line-height:1.2}
  .back-contact li{display:flex;align-items:flex-start;gap:10px;margin-top:6px}
  .back-contact svg{width:22px;height:22px;flex:none;margin-top:1px}
</style>
</head>
<body>

<section class="card card--front" aria-label="Card front">
  <svg class="card__art" viewBox="0 0 520 520" aria-hidden="true">
    <rect x="50" y="82" width="425" height="398" fill="none" stroke="var(--orange)" stroke-width="2"/>
    <polygon points="0,0 275,0 520,420 520,520 300,520 0,190" fill="var(--green)"/>
    <polyline points="50,300 50,480 330,480" fill="none" stroke="var(--orange)" stroke-width="2"/>
  </svg>
  <div class="front-logo">
    <div class="front-logo__name">TELMORO</div>
    <div class="front-logo__sub">TELMORO LIMITED</div>
  </div>
  <ul class="front-contact">
    <li><span class="front-contact__key">N</span>Mara Kellan</li>
    <li><span class="front-contact__key">A</span>Street, Area, Postal code</li>
    <li><span class="front-contact__key">P</span>+00-000 000 000</li>
    <li><span class="front-contact__key">M</span>info@mailbox.com</li>
  </ul>
</section>

<section class="card card--back" aria-label="Card back">
  <svg class="card__art" viewBox="0 0 520 520" aria-hidden="true">
    <rect x="0" y="506" width="175" height="14" fill="var(--sky)"/>
    <rect x="175" y="506" width="175" height="14" fill="var(--blue)"/>
    <rect x="350" y="506" width="170" height="14" fill="var(--navy)"/>
  </svg>
  <div class="back-logo">
    <div class="back-logo__name">TELMORO</div>
    <div class="back-logo__sub">TELMORO LIMITED</div>
  </div>
  <ul class="back-contact">
    <li><svg viewBox="0 0 22 22"><circle cx="11" cy="11" r="11" fill="var(--ink)"/><circle cx="11" cy="8.5" r="3.5" fill="#fff"/><path d="M5 17c1-3.5 11-3.5 12 0z" fill="#fff"/></svg>Mara Kellan</li>
    <li><svg viewBox="0 0 22 22"><circle cx="11" cy="11" r="11" fill="var(--ink)"/><circle cx="11" cy="11" r="5" fill="none" stroke="#fff" stroke-width="2"/></svg>Street, Area,<br>Postal code</li>
    <li><svg viewBox="0 0 22 22"><circle cx="11" cy="11" r="11" fill="var(--ink)"/><path d="M7 6l2.5 0 1 3-1.5 1c.8 1.6 1.8 2.6 3.4 3.4l1-1.5 3 1v2.5c-5 .4-9.8-4.4-9.4-9.4z" fill="#fff"/></svg>+00-000 000 000</li>
    <li><svg viewBox="0 0 22 22"><circle cx="11" cy="11" r="11" fill="var(--ink)"/><rect x="5" y="7" width="12" height="8" fill="none" stroke="#fff" stroke-width="1.6"/><path d="M5 7l6 5 6-5" fill="none" stroke="#fff" stroke-width="1.6"/></svg>info@mailbox.com</li>
  </ul>
</section>

</body>
</html>
```